Luxury Court Haven/academy - Webdesign

We want to develop a cutting edge website for a luxury tennis academy. Academy is based in Russia and includes all the necessary amenities for comfortable stay: apartments, spa, tennis courts, training facilities, etc.
We would like to see a clean, simple and modern design (with implementation of all the current trends in web design, although our project has to be distinct and unique).
Color scheme: we would like to see colors present in our logos and all the current associated with tennis. We are open to your ideas and creativity on this front.
The final design should communicate simplicity, be user friendly and convey premium feel.
We woud like to see unique ideas in the design, unconventional techniques, etc.
We don't want standard template design!
Updates
We want to mention that this Tennis Academy has a light focus on nature, as the new material we have uploaded illustrates.
Additional comment to everyone!
We couldn't upload this file to the system: it is too big.
Thank you everyone for your submissions!
Industry/Entity Type
Training
Requirements
Must have
- We would like to see the designs for the following pages:
Home Page:
- Slideshow
- Short description and all the standard stuff
About Us:
- Description with some images
Services:
- Simple description of all of the provided services and possibility to book all of them on the website
! Important ! Develop small system for booking of the days of stay and registration for the courses
Booking and registration !
News:
- Creative layout to display recent news of the academy
Coaches:
- Image and short description of our staff.
Club / Gallery:
- Images and descriptions of the amenities in the territory.
We want a unique display of images: not just lines and rows filled with images
- One idea: an interactive map that displays images and description on mouseover or click on the object on the map (but again, we are open to all your ideas)
Contacts:
- Contact form, contacts, etc.
Sport Store:
- Basic layout for the goods and services provided by the sports store located in the academy
Prices:
- Price lists and ranges with a button leading to registration and booking
For pages like About Us and Services, it would be enough to develop one unified layout for all of them.

```html
<!DOCTYPE html>
<html lang="en">
<head>
<meta charset="utf-8">
<title>Court Haven – Home</title>
<link href="https://fonts.googleapis.com/css2?family=Ubuntu:wght@400;500;700&display=swap" rel="stylesheet">
<style>
:root{
  --green:#6fb52c;
  --green-dark:#3f9a3a;
  --green-deep:#2d8a35;
  --bg:#6c665f;
  --panel:#eeeeee;
  --text:#4a4a4a;
  --footer:#3b3b3b;
  --white:#ffffff;
}
*{margin:0;padding:0;box-sizing:border-box}
html,body{width:1200px;height:981px;overflow:hidden}
body{position:relative;background:radial-gradient(ellipse at 50% 40%,#7a736b 0%,var(--bg) 60%,#5d5852 100%);font-family:"Ubuntu",sans-serif;color:var(--text)}
.abs{position:absolute}
.hero{left:0;top:0;width:1200px;height:458px;background:linear-gradient(180deg,#8d8583 0%,#b9b2ad 25%,#c9c3bf 45%,#9a4a45 75%,#8a3d3a 100%);-webkit-mask-image:linear-gradient(90deg,transparent 0,#000 18%,#000 82%,transparent 100%);mask-image:linear-gradient(90deg,transparent 0,#000 18%,#000 82%,transparent 100%)}
.navbar{left:0;top:29px;width:1200px;height:57px;background:linear-gradient(180deg,#7dbd38,#62a829);border-top:1px solid #8fd04a;border-bottom:1px solid #4f8f20}
.nav{left:389px;top:48px;display:flex;gap:0;list-style:none}
.nav li{font-weight:500;font-size:13px;color:var(--white);height:20px;line-height:20px}
.nav .active{background:var(--green-dark);padding:0 12px}
.logo{left:222px;top:0;width:154px;height:136px;background:var(--white);clip-path:polygon(0 0,100% 0,100% 100%,50% 88%,0 100%);display:flex;align-items:center;justify-content:center;gap:6px;padding-bottom:14px}
.logo span{font-weight:700;font-size:19px;color:var(--green-deep);line-height:1.05;text-align:center}
.logo i{width:14px;height:14px;border-radius:50%;background:var(--green)}
.arrow{width:38px;height:38px;top:255px}
.main{left:220px;top:458px;width:760px;height:452px;background:var(--panel);border-top:4px solid var(--green-dark);border-bottom:4px solid var(--green-dark)}
.welcome{left:230px;top:470px;font-size:15px;font-weight:500;color:#333}
.welcome b{color:var(--green-deep);font-weight:500}
.intro{left:230px;top:500px;width:546px;font-size:10px;line-height:14.4px;text-align:justify}
.intro p+p{margin-top:14.4px}
.services{left:788px;top:471px;width:183px;height:133px;background:var(--white);border:1px solid #d6d6d6}
.services h3{height:20px;margin:1px;background:var(--green);color:#2f5c10;font-weight:400;font-size:12px;line-height:20px;padding-left:6px;border:1px solid #5a9a20}
.services li{list-style:none;height:22.4px;line-height:22.4px;font-size:10px;color:#333;padding-left:14px;border-bottom:1px dashed #d8d8d8;position:relative}
.services li:last-child{border:0}
.services li::before{content:"›";position:absolute;left:4px;color:#999}
.tile{top:616px;width:178px;height:167px;background:var(--white);border:1px solid #d8d8d8;border-radius:3px;padding:6px}
.tile .photo{height:153px;position:relative}
.tile .label{position:absolute;left:0;right:0;bottom:0;height:23px;line-height:23px;text-align:center;color:var(--white);font-size:14px}
.divider{top:798px;height:1px;border-top:1px dotted #888}
.plus{top:791px;width:15px;height:15px;border-radius:50%;background:#8a8a8a;color:#fff;font-size:13px;line-height:14px;text-align:center;font-weight:700}
.news{left:230px;top:816px;width:364px;height:80px;background:var(--white);border:1px solid #d8d8d8;border-radius:3px;padding:8px 7px}
.news h4{font-weight:400;font-size:12px;color:var(--green-deep)}
.news p{font-size:10px;line-height:14.4px;color:#666;text-align:justify;margin-top:3px}
.news time{display:block;font-size:9px;color:#5b8a10;margin-top:4px}
.cta{top:816px;width:177px;height:81px;background:linear-gradient(180deg,#e6e6e6,#d0d0d0);border:1px solid #b5b5b5;border-radius:3px;box-shadow:inset 0 -2px 0 #9a9a9a;text-align:center;padding-top:6px}
.cta h4{font-weight:400;font-size:15px;line-height:22px;color:#555;letter-spacing:.5px}
.cta a{display:inline-block;margin-top:3px;width:104px;height:18px;line-height:18px;background:var(--green);border:1px solid #4b8e1d;color:var(--white);font-size:12px;text-decoration:none}
.footer{left:0;top:924px;width:1200px;height:57px;background:var(--footer)}
.flinks{left:223px;top:934px;display:flex;list-style:none;font-size:11px;color:var(--white)}
.flinks li+li::before{content:"|";margin:0 18px}
.copy{left:222px;top:957px;font-size:10px;color:#cfcfcf}
.social{top:939px;width:26px;height:26px;border-radius:50%;background:#f4f4f4;border:2px solid #ddd}
.social i{position:absolute;left:6px;top:6px;width:10px;height:10px;border-radius:50%}
</style>
</head>
<body>
<div class="abs hero" role="img" aria-label="Photo of a coach guiding a young player on an exercise bike in a gym with a red floor"></div>
<div class="abs navbar"></div>
<ul class="abs nav">
  <li class="active">Home</li>
  <li style="margin-left:10px">About Us</li>
  <li style="margin-left:20px">Services</li>
  <li style="margin-left:23px">News</li>
  <li style="margin-left:23px">Coaches</li>
  <li style="margin-left:22px">Gallery</li>
  <li style="margin-left:23px">Contacts</li>
  <li style="margin-left:23px">Store</li>
  <li style="margin-left:23px">Prices</li>
</ul>
<div class="abs logo"><span>COURT<br>HAVEN</span><i></i></div>

<svg class="abs arrow" style="left:13px" viewBox="0 0 38 38"><circle cx="19" cy="19" r="17.5" fill="#555" stroke="#ddd" stroke-width="2"/><path d="M22 11 14 19 22 27" fill="none" stroke="#fff" stroke-width="3.5"/></svg>
<svg class="abs arrow" style="left:1148px" viewBox="0 0 38 38"><circle cx="19" cy="19" r="17.5" fill="#555" stroke="#ddd" stroke-width="2"/><path d="M16 11 24 19 16 27" fill="none" stroke="#fff" stroke-width="3.5"/></svg>

<div class="abs main"></div>
<h1 class="abs welcome">» Welcome to <b>Court Haven</b></h1>
<div class="abs intro">
  <p>Lorem Ipsum is simply dummy text of the printing and typesetting industry. Lorem Ipsum has been the industry's standard dummy text ever since the 1500s, when an unknown printer took a galley of type and scrambled it to make a type specimen book. It has survived not only five centuries, but also the leap into electronic typesetting, remaining essentially unchanged.</p>
  <p>It was popularised in the 1960s with the release of Typeset sheets containing Lorem Ipsum passages, and more recently with desktop publishing software like Folio Layout including versions of Lorem Ipsum.</p>
</div>
<div class="abs services">
  <h3>» Services</h3>
  <ul><li>Lorem Ipsum 1</li><li>Lorem Ipsum 2</li><li>Lorem Ipsum 3</li><li>Lorem Ipsum 4</li><li>Lorem Ipsum 5</li></ul>
</div>

<div class="abs tile" style="left:229px"><div class="photo" role="img" aria-label="Photo of children training on an outdoor clay court" style="background:linear-gradient(180deg,#5f8a4a,#a3935f 60%,#6fa04a)"><div class="label" style="background:rgba(40,120,60,.85)">Our Programs</div></div></div>
<div class="abs tile" style="left:417px"><div class="photo" role="img" aria-label="Photo of a young player hitting a ball on an indoor court" style="background:linear-gradient(180deg,#bbb6b8,#4f5b4f 55%,#2f3a30)"><div class="label" style="background:rgba(180,160,40,.85)">Our Staff</div></div></div>
<div class="abs tile" style="left:606px"><div class="photo" role="img" aria-label="Photo of a coach with players at the court fence" style="background:linear-gradient(180deg,#a9c6d8,#6b8f58 40%,#9a5a45 80%)"><div class="label" style="background:rgba(120,190,70,.85)">Upcoming Events</div></div></div>
<div class="abs tile" style="left:794px"><div class="photo" role="img" aria-label="Photo of two children sitting with a plush toy and rackets" style="background:linear-gradient(180deg,#6f7a6a,#c8bfb3 50%,#8d9a80)"><div class="label" style="background:rgba(110,200,140,.85)">Gallery</div></div></div>

<div class="abs divider" style="left:230px;width:177px"></div>
<div class="abs divider" style="left:417px;width:177px"></div>
<div class="abs divider" style="left:607px;width:177px"></div>
<div class="abs plus" style="left:310px">+</div>
<div class="abs plus" style="left:496px">+</div>
<div class="abs plus" style="left:687px">+</div>

<div class="abs news">
  <h4>» Latest News</h4>
  <p>It was popularised in the 1960s with the release of Typeset sheets containing Lorem Ipsum passages, versions of Lorem Ipsum.</p>
  <time>30/10/2012</time>
</div>
<div class="abs cta" style="left:606px"><h4>Registration<br>Form</h4><a href="#">Download</a></div>
<div class="abs cta" style="left:793px"><h4>Tennis<br>Programs</h4><a href="#">Learn More</a></div>

<div class="abs footer"></div>
<ul class="abs flinks">
  <li>Home</li><li>Services</li><li>About Us</li><li>Gallery</li><li>Contact Us</li><li>Terms &amp; Condition</li><li>Privacy Policy</li>
</ul>
<p class="abs copy">© Copyright 2012 by Court Haven.</p>
<div class="abs social" style="left:885px" aria-label="Social link 1"><i style="background:#3b5b9a"></i></div>
<div class="abs social" style="left:917px" aria-label="Social link 2"><i style="background:#5ab0e0"></i></div>
<div class="abs social" style="left:949px" aria-label="Social link 3"><i style="background:#2a78b0"></i></div>
</body>
</html>
```